Minimalist Planner/Journal Design

We need a planner/journal designed for daily use in a small group. I've attached a requirements document that outlines what every page needs to have on it. I've also attached a basic rough draft that we had made in Canva but the draft needs to be redesigned to look more in line with the style we need. I've attached some sample pages from some planners we like the style of. Feel free to add your own creativity and stylistic choices but keep in mind we are trying to get a very 'clean and minimalist design'. The deliverables should be both a pdf of the 8 planner pages, as well as the photoshop/gimp/illustrator files for the project.

Font styles to use
Other font styles liked:
• You choose, but we prefer thin , basic/minimal font faces

Requirements
Must have
• Minimal Design

```html
<!DOCTYPE html>
<html lang="en">
<head>
<meta charset="utf-8">
<title>Weekly Planner Page</title>
<link href="https://fonts.googleapis.com/css2?family=Source+Sans+3:wght@300;400&display=swap" rel="stylesheet">
<style>
  :root {
    --backdrop: #c5c6c8;
    --page: #ffffff;
    --band: #888a89;
    --ink: #3a3a3a;
    --rule: #8a8a8a;
    --dot: #9a9a9a;
    --cell: #f4f4f4;
    --light-box: #c8c8c8;
  }
  * { box-sizing: border-box; margin: 0; padding: 0; }
  html, body {
    width: 1200px; height: 813px; overflow: hidden;
    background: var(--backdrop);
    font-family: "Source Sans 3", "Helvetica Neue", Arial, sans-serif;
    font-weight: 300;
    color: var(--ink);
  }
  .canvas { position: relative; width: 1200px; height: 813px; }
  .page {
    position: absolute; left: 600px; top: 52px; width: 547px; height: 709px;
    background: var(--page);
    border-radius: 0 26px 20px 0;
    border-bottom: 8px solid var(--band);
    overflow: hidden;
  }
  .page-header {
    position: absolute; left: 0; top: 0; width: 100%; height: 58px;
    background: var(--band); color: #fff;
    font-size: 12.5px; letter-spacing: 0.2px;
  }
  .week-label { position: absolute; left: 25px; top: 23px; }
  .date-slashes { position: absolute; left: 391px; top: 23px; }
  .section-title { position: absolute; left: 25px; font-size: 11px; }
  .primary-title { top: 68px; }
  .secondary-title { top: 246px; }

  .task { position: absolute; left: 25px; width: 195px; height: 45px; }
  .task .box {
    position: absolute; left: 0; top: 0; width: 10.5px; height: 10.5px;
    border: 1px solid var(--rule);
  }
  .task.faint .box { border-color: var(--light-box); }
  .task .num { position: absolute; left: 17px; top: -6px; font-size: 11px; }
  .task .main-rule {
    position: absolute; left: 17px; right: 0; top: 9px; border-top: 1px solid var(--rule);
  }
  .task .dot-rule {
    position: absolute; left: 17px; right: 0; border-top: 1px dotted var(--dot);
  }

  .secondary-lines { position: absolute; left: 25px; top: 326px; width: 195px; }
  .secondary-lines span {
    display: block; height: 18.45px; border-top: 1px solid var(--rule);
  }

  .trackers { position: absolute; left: 665px; top: 650px; list-style: none; font-size: 11px; }
  .trackers li { position: absolute; left: 0; white-space: nowrap; }
  .trackers .ring {
    position: absolute; left: 0; top: 3px; width: 8px; height: 8px;
    border: 1.2px solid var(--rule); border-radius: 50%;
  }
  .trackers .text { position: absolute; left: 22px; top: 0; }

  .schedule {
    position: absolute; left: 291px; top: 102px; width: 231px;
    border-top: 1px solid var(--rule); background: var(--cell);
  }
  .schedule .row {
    display: flex; height: 24.6px; border-bottom: 1px solid var(--rule);
    font-size: 10.5px; font-weight: 400;
  }
  .schedule .time {
    width: 65px; border-right: 1px solid var(--rule);
    display: flex; align-items: center; justify-content: center; padding-left: 4px;
  }
  .schedule .slot { flex: 1; }

  .daily-score {
    position: absolute; left: 355px; top: 666px; font-size: 11px;
    display: flex; align-items: center; gap: 6px;
  }
</style>
</head>
<body>
<div class="canvas">
  <section class="page">
    <header class="page-header">
      <span class="week-label">WEEK</span>
      <span class="date-slashes">//</span>
    </header>

    <h2 class="section-title primary-title" style="font-weight:300">PRIMARY TASKS</h2>
    <div class="task" style="top:93px">
      <span class="box"></span><span class="num">1</span>
      <span class="main-rule"></span>
      <span class="dot-rule" style="top:21px"></span>
      <span class="dot-rule" style="top:34px"></span>
    </div>
    <div class="task faint" style="top:142px">
      <span class="box"></span><span class="num">2</span>
      <span class="main-rule"></span>
      <span class="dot-rule" style="top:21px"></span>
      <span class="dot-rule" style="top:33px"></span>
    </div>
    <div class="task faint" style="top:191px">
      <span class="box"></span><span class="num">3</span>
      <span class="main-rule"></span>
      <span class="dot-rule" style="top:21px"></span>
      <span class="dot-rule" style="top:33px"></span>
    </div>

    <h2 class="section-title secondary-title" style="font-weight:300">SECONDARY&nbsp; TASKS</h2>
    <div class="secondary-lines" style="top:274px">
      <span></span><span></span><span></span><span></span><span></span><span></span>
      <span></span><span></span><span></span><span></span><span></span><span></span>
      <span></span><span></span><span></span><span></span><span></span>
    </div>

    <div class="schedule">
      <div class="row"><span class="time">5 AM</span><span class="slot"></span></div>
      <div class="row"><span class="time">6 AM</span><span class="slot"></span></div>
      <div class="row"><span class="time">7 AM</span><span class="slot"></span></div>
      <div class="row"><span class="time">8 AM</span><span class="slot"></span></div>
      <div class="row"><span class="time">9 AM</span><span class="slot"></span></div>
      <div class="row"><span class="time">10 AM</span><span class="slot"></span></div>
      <div class="row"><span class="time">11 AM</span><span class="slot"></span></div>
      <div class="row"><span class="time">12 PM</span><span class="slot"></span></div>
      <div class="row"><span class="time">1&nbsp; PM</span><span class="slot"></span></div>
      <div class="row"><span class="time">2&nbsp; PM</span><span class="slot"></span></div>
      <div class="row"><span class="time">3&nbsp; PM</span><span class="slot"></span></div>
      <div class="row"><span class="time">4&nbsp; PM</span><span class="slot"></span></div>
      <div class="row"><span class="time">5&nbsp; PM</span><span class="slot"></span></div>
      <div class="row"><span class="time">6&nbsp; PM</span><span class="slot"></span></div>
      <div class="row"><span class="time">7&nbsp; PM</span><span class="slot"></span></div>
      <div class="row"><span class="time">8&nbsp; PM</span><span class="slot"></span></div>
      <div class="row"><span class="time">9&nbsp; PM</span><span class="slot"></span></div>
      <div class="row"><span class="time">10&nbsp; PM</span><span class="slot"></span></div>
      <div class="row"><span class="time">10&nbsp; PM</span><span class="slot"></span></div>
      <div class="row"><span class="time">10&nbsp; PM</span><span class="slot"></span></div>
      <div class="row"><span class="time">10&nbsp; PM</span><span class="slot"></span></div>
      <div class="row"><span class="time">10&nbsp; PM</span><span class="slot"></span></div>
    </div>

    <div class="daily-score">
      <span>DAILY SCORE W/L</span>
      <svg width="9" height="9" viewBox="0 0 9 9" aria-hidden="true">
        <rect x="0.5" y="1.5" width="7" height="7" fill="none" stroke="#666" stroke-width="0.9"/>
        <path d="M2 4.8 L3.8 6.5 L8.5 1" fill="none" stroke="#666" stroke-width="0.9"/>
      </svg>
    </div>
  </section>

  <ul class="trackers">
    <li style="top:0"><span class="ring"></span><span class="text">PHYSICAL ACTIVITY</span></li>
    <li style="top:18px"><span class="ring"></span><span class="text">HABIT</span></li>
    <li style="top:36px"><span class="ring"></span><span class="text">WEEKLY CHALLENGE</span></li>
  </ul>
</div>
</body>
</html>
```